AUSTRALIA SUPPLEMENT - Protein label design - CREATIVE, FEMININE, UNIQUE

I need help with the design of what will be my line of supplements. (Protein, plant base, collagen , BCAAs, etc)
I'm starting off with protein isolate - with the flavours VANILLA, CHOCOLATE, BOYSENBERRY, HONEYCOMB.
I need help with the design of what the product will look like for my range.
(Great opportunity for further work)

Looking for a unique, elegant, stand out, feminine design, some slight sparkle or something that stands out on a shelf.
With symbols to represent what's in it, raised text. with some quirky cute things on it. (not sure what) Something that captured young womens eyes and easy to understand. things on it that appeals to women such as
LOW CALORIE, GREAT TASTING, GLUTEN FREE, 100 NATURAL, NATURALLY SWEETENED, HIGH PROTEIN.etc and whatever you can think of (open to ideas) but within PCF guidelines.

Mostly just after the look and creativity of what the front will look like. Don't have to worry about the back area.

My market will be for females aged 18-35

I have a activewear line called BRONTUK which will go with this. which I will attach the logo below amongst some other things that match my packaging. (again open to ideas)

I have attached a label of what one will look like( EXAMPLE).
. Among others that look nice But again I want to be different, unique to stand out. I don't want it to look like these. it's just the only ones I found online I liked that suit my market.

Feel free to ask any questions! :)
Updates

Extending time as I want this to be to be what will be on the shelves of many stores. I know that needs time to be able to do a quality job.

Target Market(s)

18-35

Industry/Entity Type

Supplement

Font styles to use
Serif
Script

Colors
f9d9e8
ffffff
fbd3d4
ecf7fb
e4daeb
cfeae6
eea4c8
fdfad7
f59195

Requirements
Must have
• Word - BRONTUK
PROTEIN ISOLATE
FLAVOUR
SYMBOLS

Looking for a unique, elegant, stand out, colour, feminine design, some slight sparkle or something that stands out on a shelf.

IT WILL BE ON A WHITE TUB or CLEAR - Perhaps detail on the lid
Nice to have
• Looking for a unique, elegant, stand out, colour, feminine design, some slight sparkle or something that stands out on a shelf. Something artsy.

will be on a white or clear tub with a white label background (possibly)
Should not have
• I don’t want it dark looking.
Something bright, vibrant, whites, pinks, sparkles (maybe) colours.

I don't want the word activewear on it.

```html
<!DOCTYPE html>
<html lang="en">
<head>
<meta charset="utf-8">
<title>BRONTUK W.P.I. Vanilla Label</title>
<link rel="stylesheet" href="https://fonts.googleapis.com/css2?family=Cinzel:wght@400&family=Great+Vibes&family=Montserrat:wght@400;500&display=swap">
<style>
  :root {
    --backdrop: #fbeef4;
    --label-white: #fdfcfb;
    --panel-pink: #f6cfe2;
    --brand-pink: #f4b8d8;
    --type-pink: #ec9fca;
    --badge-pink: #f0a6cc;
    --mint: #cfeae6;
    --white: #ffffff;
  }
  * { margin: 0; padding: 0; box-sizing: border-box; }
  html, body { width: 1200px; height: 799px; overflow: hidden; }
  body { background: var(--backdrop); position: relative; }

  .label {
    position: absolute; left: 100px; top: 6px;
    width: 1000px; height: 788px;
    background: var(--label-white);
    overflow: hidden;
  }
  .side-panel {
    position: absolute; top: 0; height: 100%; width: 150px;
    background: linear-gradient(180deg, #f8d8e7 0%, var(--panel-pink) 100%);
  }
  .side-panel--left { left: 0; }
  .side-panel--right { right: 0; }

  .brand-tab {
    position: absolute; left: 392px; top: 0;
    width: 225px; height: 212px;
    background: var(--brand-pink);
    border-radius: 0 0 30px 30px;
    display: flex; flex-direction: column; align-items: center; justify-content: center; gap: 16px;
  }
  .brand-dot { width: 18px; height: 18px; border-radius: 50%; background: var(--white); }
  .brand-name {
    font-family: "Cinzel", serif; font-weight: 400;
    font-size: 30px; letter-spacing: 5px; color: var(--white);
  }

  .product-code {
    position: absolute; left: 150px; width: 700px; top: 232px;
    text-align: center;
    font-family: "Montserrat", sans-serif; font-weight: 400;
    font-size: 164px; line-height: 1; letter-spacing: 6px;
    color: var(--type-pink);
  }
  .product-name {
    position: absolute; left: 150px; width: 700px; top: 405px;
    text-align: center;
    font-family: "Great Vibes", cursive;
    font-size: 80px; line-height: 1; color: var(--type-pink);
  }

  .flavour-band {
    position: absolute; left: 0; top: 512px; width: 100%; height: 106px;
    background: linear-gradient(90deg, #c9e8e3 0%, #e3f4f2 50%, #c9e8e3 100%);
    display: flex; align-items: center; justify-content: center;
  }
  .flavour-name {
    font-family: "Montserrat", sans-serif; font-weight: 400;
    font-size: 46px; letter-spacing: 40px; margin-right: -40px;
    color: var(--white);
  }

  .claim {
    position: absolute; top: 650px;
    width: 100px; height: 100px; border-radius: 50%;
    background: var(--badge-pink);
    display: flex; align-items: center; justify-content: center;
    text-align: center;
    font-family: "Montserrat", sans-serif; font-weight: 500;
    font-size: 14px; line-height: 1.25; color: var(--white);
  }
  .claim--calorie { left: 224px; }
  .claim--gluten { left: 376px; }
  .claim--natural { left: 532px; }
  .claim--protein { left: 676px; }
</style>
</head>
<body>
  <main class="label">
    <div class="side-panel side-panel--left" role="img" aria-label="Pink panel with a pattern of leafy branches"></div>
    <div class="side-panel side-panel--right" role="img" aria-label="Pink panel with a pattern of leafy branches"></div>

    <div class="brand-tab">
      <span class="brand-dot"></span>
      <span class="brand-name">BRONTUK</span>
    </div>

    <h1 class="product-code">W.P.I.</h1>
    <p class="product-name">Whey Protein Isolate</p>

    <div class="flavour-band"><span class="flavour-name">VANILLA</span></div>

    <div class="claim claim--calorie">LOW<br>CALORIE</div>
    <div class="claim claim--gluten">GLUTEN<br>FREE</div>
    <div class="claim claim--natural">100<br>NATURAL</div>
    <div class="claim claim--protein">HIGH<br>PROTEIN</div>
  </main>
</body>
</html>
```